MOV Promotional flyer for students

We're looking for an 8.5" x 11" flyer that will be distributed to schools. Please see language to include in attached files.

Target Market(s)

The parents and teachers of high school students

Industry/Entity Type

Mental health

Other font styles liked:
• Monserrat and Roboto Slab

Requirements
Must have
• See attached pdf for language to be included on the flyer. Please use the color palette from our website: www.lumemov.tv. Please include some imagery of students. Please ensure the
Nice to have
• Feel free to use any of the graphics provided. See our website for our brand look & feel: www.lumemov.tv

```html
<!DOCTYPE html>
<html lang="en">
<head>
<meta charset="utf-8">
<title>Fundraise with MOV</title>
<link href="https://fonts.googleapis.com/css2?family=Montserrat:wght@600;700;800;900&display=swap" rel="stylesheet">
<style>
  :root {
    --orange: #f58a2e;
    --orange-logo: #f27e35;
    --peach: #fac89a;
    --navy: #276a93;
    --sky: #6aa3c4;
    --bright-blue: #31a0e0;
    --slate: #5f6b62;
    --white: #ffffff;
    --ink: #111111;
  }
  html, body {
    margin: 0;
    padding: 0;
    width: 927px;
    height: 1200px;
    overflow: hidden;
    background: var(--orange);
  }
  .flyer {
    position: relative;
    width: 927px;
    height: 1200px;
    overflow: hidden;
    background: var(--orange);
    font-family: "Montserrat", Arial, sans-serif;
  }
  .shapes {
    position: absolute;
    inset: 0;
  }
  .headline {
    position: absolute;
    left: 52px;
    top: 52px;
    width: 560px;
    margin: 0;
    color: #fdf3ef;
    font-weight: 900;
    font-size: 88px;
    line-height: 1;
    letter-spacing: -1px;
  }
  .headline .with {
    display: block;
    text-align: right;
    font-size: 27px;
    letter-spacing: 0;
    margin-top: 6px;
  }
  .brand-name {
    position: absolute;
    left: 642px;
    top: 96px;
    width: 206px;
    text-align: center;
    color: var(--white);
    font-weight: 800;
    font-size: 72px;
    line-height: 1;
    letter-spacing: -2px;
  }
  .badge {
    position: absolute;
    left: 102px;
    top: 282px;
    width: 274px;
    text-align: center;
    color: var(--navy);
    font-weight: 900;
  }
  .badge .percent {
    display: block;
    font-size: 82px;
    line-height: 1;
    letter-spacing: -3px;
  }
  .badge .proceeds {
    display: block;
    color: var(--orange);
    font-size: 18px;
    margin-top: 6px;
  }
  .badge .school {
    display: block;
    font-size: 26px;
    line-height: 1.05;
    margin-top: 8px;
    letter-spacing: -0.5px;
  }
  .cause {
    position: absolute;
    left: 98px;
    top: 618px;
    margin: 0;
    color: var(--white);
    font-weight: 800;
    font-size: 46px;
    line-height: 55px;
    letter-spacing: 1px;
  }
  .about {
    position: absolute;
    left: 68px;
    top: 966px;
    width: 508px;
    margin: 0;
    text-align: center;
    color: var(--ink);
    font-weight: 700;
    font-size: 15.6px;
    line-height: 32px;
  }
  .site {
    position: absolute;
    left: 618px;
    top: 1040px;
    width: 267px;
    height: 40px;
    border-radius: 20px;
    background: var(--orange);
    color: var(--white);
    font-weight: 900;
    font-size: 25px;
    line-height: 40px;
    text-align: center;
    letter-spacing: -0.5px;
  }
</style>
</head>
<body>
<main class="flyer">
  <svg class="shapes" width="927" height="1200" viewBox="0 0 927 1200" xmlns="http://www.w3.org/2000/svg">
    <defs>
      <linearGradient id="photoTone" x1="0" y1="0" x2="1" y2="1">
        <stop offset="0" stop-color="#c9cdcc"/>
        <stop offset="0.35" stop-color="#5a3a2c"/>
        <stop offset="0.6" stop-color="#8fb3cf"/>
        <stop offset="1" stop-color="#2b1d18"/>
      </linearGradient>
    </defs>

    <!-- top-right peach wedge -->
    <polygon points="530,0 927,0 927,60 700,230" fill="var(--peach)"/>

    <!-- student photo area -->
    <polygon points="362,220 927,220 927,1200 365,1200 240,880 160,540" fill="url(#photoTone)" role="img" aria-label="Photo of two smiling high school students looking at a tablet together"/>

    <!-- top-right circles -->
    <circle cx="725" cy="47" r="104" fill="var(--navy)"/>
    <circle cx="860" cy="181" r="146" fill="var(--sky)"/>

    <!-- brand circle -->
    <circle cx="745" cy="136" r="104" fill="var(--white)"/>
    <circle cx="745" cy="136" r="101" fill="var(--orange-logo)"/>

    <!-- badge -->
    <circle cx="170" cy="329" r="115" fill="var(--navy)"/>
    <circle cx="239" cy="378" r="139" fill="var(--orange)"/>
    <circle cx="239" cy="378" r="134" fill="var(--white)"/>

    <!-- slate triangle -->
    <polygon points="14,527 198,527 14,730" fill="var(--slate)"/>
    <polygon points="143,527 198,527 160,572" fill="#4a7fa6"/>

    <!-- bottom-left circles -->
    <circle cx="121" cy="985" r="154" fill="var(--navy)"/>
    <circle cx="55" cy="1185" r="132" fill="var(--sky)"/>

    <!-- cause panel -->
    <polygon points="52,590 447,590 595,747 595,873 52,873" fill="var(--bright-blue)"/>
    <polygon points="65,577 456,577 604,731 604,856 65,856" fill="none" stroke="var(--orange)" stroke-width="4"/>

    <!-- about box -->
    <polygon points="98,928 587,928 587,1128 43,1128 43,983" fill="var(--white)" stroke="var(--orange)" stroke-width="5"/>

    <!-- bottom-right circles -->
    <circle cx="675" cy="1032" r="102" fill="var(--navy)"/>
    <circle cx="845" cy="1094" r="132" fill="var(--sky)"/>

    <!-- web marker -->
    <circle cx="752" cy="1057" r="62" fill="none" stroke="var(--white)" stroke-width="7"/>
  </svg>

  <h1 class="headline">FUNDRAISE<span class="with">WITH</span></h1>
  <div class="brand-name">mov</div>

  <div class="badge">
    <span class="percent">50%</span>
    <span class="proceeds">OF ALL PROCEEDS</span>
    <span class="school">GO BACK TO<br>YOUR SCHOOL</span>
  </div>

  <h2 class="cause">SUPPORT<br>THE MENTAL<br>HEALTH OF<br>YOUR STUDENTS</h2>

  <p class="about">MOV is a simple and effective way to improve mental health. Your students will learn valuable coping skills and techniques from expert clinicians who analyze real cases and share their insights and advice.</p>

  <div class="site">LUMEMOV.TV</div>
</main>
</body>
</html>
```